Redesign of TaskHarbor.com website

Our website was initially developed 6+ years ago and has been maintained by several different designers. As a result, it is overly complex, inconsistent format/layout and the content is not well structured/easy to navigate

We need the site redeveloped with a more modern look and feel, simpler content structure and ability to implement new/improved tools, such as: Dynamic Forms, Sales Funnels, Landing Pages, improved metadata of our pages and posts, improved SEO/Page ranking, etc.

We currently use DealRiver CRM, Steady Reach for marketing automation and GridPilot forms. We are investigating Floxen for workflow integration which could extend to our website.

Our current website is developed in WordPress, ideally we will stick with this platform, but we’re happy to consider other CMS' if strongly recommended. We may decide to remove/consolidate some of the pages and/or content as part of this re-design.

We don't want to rebrand (ie change corporate logo, colours scheme etc) as part of this website redevelopment and it is critical that we don't lose our current Page Ranking, SEO rankings, backlink benefits, etc as part of this redevelopment.

Sites we like the feel/design of are: boardwiley.com, tallypoint.com and rankgrove.com

Target Market(s)

Corporate, Enterprise and Government B2B clients.

Coding

Coded - Design and coding required

Number of Pages Required

5+ page

Font styles to use
Sans Serif

Colors
ffffff
ec1f27

Requirements
Must have
• Must retain the majority of content on our existing website (although we may re-write some of it as part of this redesign process).
Nice to have
• See above "Project Description"
Should not have

```html
<!DOCTYPE html>
<html lang="en">
<head>
<meta charset="utf-8">
<title>TaskHarbor – Your trusted advisor</title>
<link rel="stylesheet" href="https://fonts.googleapis.com/css2?family=Poppins:wght@400;500;600;700;800&family=Montserrat:wght@800;900&family=Barlow:wght@400;500;600;700&display=swap">
<style>
:root{
  --red:#ec1f27;
  --red-deep:#d0141b;
  --navy:#1c2330;
  --navy-2:#28313f;
  --slate:#4b535c;
  --grey-deco:#c4c4c4;
  --grey-bg:#f3f3f3;
  --ink:#1b1b1b;
  --text:#3a3a3a;
  --muted:#8a8f96;
  --white:#ffffff;
}
*{margin:0;padding:0;box-sizing:border-box}
html,body{width:1200px;height:4129px;overflow:hidden}
body{position:relative;background:var(--white);font-family:"Barlow",Arial,sans-serif;color:var(--text)}
.abs{position:absolute}

/* hero */
.hero{position:absolute;left:0;top:0;width:1200px;height:559px;background:linear-gradient(160deg,#222b38 0%,#1a212c 60%,#1d2531 100%);overflow:hidden}
.brand{position:absolute;display:flex;align-items:center;gap:10px}
.brand-dot{width:30px;height:30px;border-radius:50%;background:var(--red)}
.brand-name{font-family:"Poppins",sans-serif;font-weight:500;font-size:30px;line-height:1;color:var(--white);letter-spacing:-.5px}
.brand-tag{font-family:"Barlow",sans-serif;font-size:10px;color:#c9ccd1;text-align:right;margin-top:1px}
.nav a{position:absolute;top:50px;font-family:"Barlow",sans-serif;font-size:12px;color:#e6e8eb;text-decoration:none;letter-spacing:.3px}
.nav .nav-cta{top:43px;left:895px;width:93px;height:24px;background:var(--white);color:var(--ink);font-weight:700;font-size:11px;display:flex;align-items:center;justify-content:center}
.burger{position:absolute;left:1016px;top:47px;width:20px;height:14px;border-top:2px solid #fff;border-bottom:2px solid #fff}
.burger::after{content:"";position:absolute;left:0;right:0;top:4px;border-top:2px solid #fff}
.hero-title{position:absolute;left:163px;top:142px;width:470px;font-family:"Poppins",sans-serif;font-weight:700;font-size:45px;line-height:50px;color:var(--white);letter-spacing:-.3px}
.hero-sub{position:absolute;left:163px;top:308px;width:450px;font-size:17px;line-height:26px;color:#e4e6ea}
.btn{display:flex;align-items:center;justify-content:center;font-family:"Poppins",sans-serif;font-weight:700;text-transform:uppercase;letter-spacing:.3px}
.btn-red{background:var(--red);color:var(--white)}
.hero-btn{position:absolute;left:163px;top:375px;width:131px;height:34px;font-size:11px}
.hero-photo{position:absolute;left:654px;top:135px;width:459px;height:306px;background:linear-gradient(135deg,#d9d4cb 0%,#8a6a4c 45%,#5d4634 70%,#b8b2a8 100%)}
.seen{position:absolute;left:163px;top:508px;width:560px;height:20px;color:#d7dade}
.seen-label{position:absolute;left:0;top:4px;font-size:8px;font-weight:600;letter-spacing:.4px}
.seen-name{position:absolute;top:0;font-family:"Poppins",sans-serif;font-weight:600;font-size:13px;line-height:18px;color:#d7dade;white-space:nowrap}

/* services */
.svc{position:absolute}
.svc h3{font-family:"Poppins",sans-serif;font-weight:500;font-size:14px;color:var(--ink);margin-bottom:5px;line-height:18px}
.svc ul{list-style:none}
.svc li{position:relative;padding-left:18px;font-size:10.5px;line-height:16.8px;color:#4a4a4a}
.svc li::before{content:"";position:absolute;left:0;top:3px;width:10px;height:10px;border:1.3px solid #555}
.svc li::after{content:"";position:absolute;left:4px;top:2px;width:4px;height:8px;border-right:1.6px solid #333;border-bottom:1.6px solid #333;transform:rotate(40deg)}
.svc .btn{width:90px;height:20px;font-size:9px;margin-top:8px}

/* partners */
.partners-bg{position:absolute;left:0;top:1149px;width:1200px;height:1252px;background:var(--grey-bg)}
.partners-card{position:absolute;left:210px;top:1182px;width:780px;height:1181px;background:var(--white)}
.partners-title{position:absolute;left:264px;top:1226px;font-family:"Montserrat",sans-serif;font-weight:900;font-size:52px;line-height:54px;color:var(--ink);letter-spacing:.3px}
.partners-title .strike{position:relative}
.partners-title .strike::after{content:"";position:absolute;left:-4px;right:-2px;top:27px;border-top:4px solid var(--red)}
.partners-title .accent{color:var(--red)}
.client{position:absolute;transform:translateX(-50%);display:flex;align-items:center;gap:6px;font-family:"Poppins",sans-serif;font-weight:600;font-size:14px;color:#7b7f85;white-space:nowrap}
.client i{display:block;width:12px;height:12px;background:#7b7f85}
.tile{position:absolute}
.tile-name{display:flex;align-items:center;justify-content:center;font-family:"Poppins",sans-serif;font-weight:600;font-size:30px;color:var(--white);letter-spacing:1px}
.btn-outline{background:var(--white);color:var(--ink);border:1px solid #cfcfcf}

/* how we work */
.work{position:absolute;left:0;top:2401px;width:1200px;height:571px;background:var(--slate)}
.work-title{position:absolute;left:0;width:1200px;top:2466px;text-align:center;font-family:"Poppins",sans-serif;font-weight:700;font-size:42px;color:var(--white)}
.work-intro{position:absolute;left:200px;width:800px;top:2522px;text-align:center;font-size:12px;line-height:19px;color:#e0e2e5}
.step{position:absolute;top:2590px;width:280px;height:286px;background:var(--white);text-align:center}
.step svg{position:absolute;left:88px;top:37px}
.step h4{position:absolute;left:0;right:0;top:154px;font-family:"Poppins",sans-serif;font-weight:700;font-size:21px;color:var(--ink)}
.step p{position:absolute;left:16px;right:16px;top:192px;font-size:9.5px;line-height:15px;color:#555}

/* testimonial */
.person{position:absolute;left:184px;top:2991px;width:325px;height:442px;background:linear-gradient(180deg,#eef0f3 0%,#c8ccd3 40%,#2b3950 75%,#23304a 100%)}
.t-title{position:absolute;left:557px;top:3095px;font-family:"Poppins",sans-serif;font-weight:700;font-size:42px;line-height:47px;color:var(--ink)}
.t-quote{position:absolute;left:560px;top:3210px;width:480px;font-family:"Poppins",sans-serif;font-size:13px;line-height:15px;color:#333}
.t-name{position:absolute;left:560px;top:3281px;font-family:"Poppins",sans-serif;font-weight:500;font-size:13px;color:#222;line-height:20px}
.arrow{position:absolute;top:3324px;width:26px;height:26px;border-radius:50%;background:var(--red)}

/* contact */
.band-red{position:absolute;left:0;top:3577px;width:1200px;height:263px;background:var(--red)}
.contact{position:absolute;left:163px;top:3433px;width:873px;height:340px;background:var(--navy)}
.c-kicker{position:absolute;left:201px;top:3464px;font-family:"Poppins",sans-serif;font-weight:700;font-size:8px;color:#fff;letter-spacing:.5px}
.c-title{position:absolute;left:201px;top:3493px;font-family:"Poppins",sans-serif;font-weight:700;font-size:31px;line-height:34px;color:#fff}
.c-text{position:absolute;left:201px;top:3573px;font-size:11.5px;color:#e2e4e7}
.c-addr{position:absolute;left:201px;top:3705px;font-size:11.5px;line-height:16px;color:#e2e4e7}
.social{position:absolute;display:flex;gap:8px}
.social span{width:15px;height:15px;border-radius:50%;background:#fff;display:block}
.field-label{position:absolute;font-size:8.5px;color:#e2e4e7}
.field{position:absolute;background:#fff}

/* footer */
.footer{position:absolute;left:0;top:3840px;width:1200px;height:289px;background:var(--navy)}
.f-about{position:absolute;left:163px;top:3884px;width:270px;font-size:10.5px;line-height:14.5px;color:#e2e4e7}
.f-links{position:absolute;list-style:none}
.f-links li{font-family:"Poppins",sans-serif;font-weight:600;font-size:7.5px;line-height:30.5px;color:#fff;letter-spacing:.2px}
.f-contact{position:absolute;right:164px;top:3936px;text-align:right;font-size:11px;line-height:15px;color:#e2e4e7}
.f-copy{position:absolute;left:163px;top:4092px;font-size:9px;color:#e2e4e7}
</style>
</head>
<body>

<!-- HERO -->
<header class="hero">
  <svg class="abs" style="left:0;top:0" width="1200" height="559" viewBox="0 0 1200 559" aria-hidden="true">
    <path d="M637 202 A103 103 0 0 1 740 99 L740 142 A60 60 0 0 0 680 202 Z" fill="var(--grey-deco)"/>
    <path d="M990 492 A210 210 0 0 1 1200 282 L1200 362 A130 130 0 0 0 1070 492 Z" fill="var(--red-deep)"/>
  </svg>
  <div class="hero-photo" role="img" aria-label="Overhead photo of a team meeting around a wooden table with laptops"></div>

  <div class="brand" style="left:163px;top:30px">
    <span class="brand-dot"></span>
    <div>
      <div class="brand-name">taskharbor</div>
      <div class="brand-tag">your trusted advisor</div>
    </div>
  </div>

  <nav class="nav">
    <a style="left:468px">HOME</a>
    <a style="left:535px">ABOUT</a>
    <a style="left:602px">SERVICES</a>
    <a style="left:692px">CLIENTS</a>
    <a style="left:759px">RESOURCES</a>
    <a style="left:851px">BLOG</a>
    <a class="nav-cta">CONTACT</a>
  </nav>
  <div class="burger"></div>

  <h1 class="hero-title">Creating value from actionable planning and strategy</h1>
  <p class="hero-sub">Utilising breakthrough digital strategies and technologies to change business for the better and go further, faster.</p>
  <a class="btn btn-red hero-btn">Get in touch</a>

  <div class="seen">
    <span class="seen-label">AS SEEN ON</span>
    <span class="seen-name" style="left:68px;font-size:15px">Lumora</span>
    <span class="seen-name" style="left:150px">Streamvale</span>
    <span class="seen-name" style="left:250px;font-size:9px;line-height:10px">Allied<br>Assembly</span>
    <span class="seen-name" style="left:326px;font-size:12px">Korvane</span>
    <span class="seen-name" style="left:412px;font-size:10px;color:#a3a8ae">Shieldpeak</span>
  </div>
</header>

<!-- SERVICES -->
<section>
  <div class="svc" style="left:160px;top:587px">
    <h3>Resilience &amp; Continuity</h3>
    <ul>
      <li>Business Continuity Management</li><li>Disaster Recovery Planning</li><li>Crisis Management</li><li>Emergency Management Planning</li><li>Workplace Health and Safety</li><li>Pandemic Response Planning</li><li>Risk Management</li><li>Strategy Development</li><li>Policy, Plan &amp; Process Development</li><li>Plan Testing and Exercising</li><li>Maintenance, Governance &amp; Compliance</li><li>Outsourcing &amp; Managed Services</li><li>Training Services</li><li>Backup &amp; Archiving Services</li>
    </ul>
    <a class="btn btn-red">Learn more</a>
  </div>
  <div class="svc" style="left:516px;top:587px">
    <h3>IT Services &amp; Solutions</h3>
    <ul>
      <li>Business Continuity Management</li><li>Disaster Recovery Planning</li><li>Crisis Management</li><li>Emergency Management Planning</li><li>Workplace Health and Safety</li><li>Pandemic Response Planning</li><li>Risk Management</li><li>Strategy Development</li><li>Policy, Plan &amp; Process Development</li><li>Plan Testing and Exercising</li><li>Maintenance, Governance &amp; Compliance</li><li>Outsourcing &amp; Managed Services</li><li>Training Services</li><li>Backup &amp; Archiving Services</li>
    </ul>
    <a class="btn btn-red">Learn more</a>
  </div>
  <div class="svc" style="left:849px;top:587px">
    <h3>Software Solutions</h3>
    <ul>
      <li>Digital Information Security Policy</li><li>Information Security Management</li><li>Cyber Security Awareness Training</li><li>Security Review and Assessment</li><li>Security Risk Management</li><li>Vulnerability Identification &amp; Testing</li><li>Penetration Testing</li><li>Network Traffic Analysis</li>
    </ul>
    <a class="btn btn-red">Learn more</a>
  </div>
  <div class="svc" style="left:160px;top:898px">
    <h3>Security Management</h3>
    <ul>
      <li>Digital Information Security Policy</li><li>Information Security Management</li><li>Cyber Security Awareness Training</li><li>Security Review and Assessment</li><li>Security Risk Management</li><li>Vulnerability Identification &amp; Testing</li><li>Penetration Testing</li><li>Network Traffic Analysis</li>
    </ul>
    <a class="btn btn-red">Learn more</a>
  </div>
  <div class="svc" style="left:516px;top:898px">
    <h3>Data Management</h3>
    <ul>
      <li>Digital Information Security Policy</li><li>Information Security Management</li><li>Cyber Security Awareness Training</li><li>Security Review and Assessment</li><li>Security Risk Management</li><li>Vulnerability Identification &amp; Testing</li><li>Penetration Testing</li><li>Network Traffic Analysis</li>
    </ul>
    <a class="btn btn-red">Learn more</a>
  </div>
</section>

<!-- PARTNERS -->
<section>
  <div class="partners-bg"></div>
  <div class="partners-card"></div>
  <svg class="abs" style="left:0;top:1100px" width="1200" height="1360" viewBox="0 1100 1200 1360" aria-hidden="true">
    <path d="M790 1362 A258 258 0 0 1 1048 1104 L1048 1232 A130 130 0 0 0 918 1362 Z" fill="var(--red-deep)"/>
    <path d="M905 1438 A123 123 0 0 1 1028 1315 L1028 1376 A62 62 0 0 0 966 1438 Z" fill="var(--grey-deco)"/>
    <path d="M0 2294 H256 Q215 2420 0 2446 Z" fill="var(--red-deep)"/>
  </svg>

  <h2 class="partners-title">WE DON’T HAVE<br><span class="strike">CLIENTS</span>, WE<br>HAVE <span class="accent">PARTNERS.</span></h2>

  <div class="client" style="left:312px;top:1451px"><i></i>Civic Builders</div>
  <div class="client" style="left:452px;top:1451px"><i></i>Northern Aid</div>
  <div class="client" style="left:593px;top:1449px;font-size:18px">Hirely</div>
  <div class="client" style="left:734px;top:1451px">Maren’s</div>
  <div class="client" style="left:873px;top:1453px;font-size:9px">Fenwick Supply</div>
  <div class="client" style="left:312px;top:1541px">Brightfold Foods</div>
  <div class="client" style="left:452px;top:1541px;font-weight:400;font-size:16px">costpal</div>
  <div class="client" style="left:593px;top:1539px;font-size:20px">Onward</div>
  <div class="client" style="left:734px;top:1541px;font-size:13px"><i></i>Quillstone Trust</div>
  <div class="client" style="left:873px;top:1544px;font-size:9px;letter-spacing:2px"><i></i>AQUAVOLT</div>

  <div class="tile" style="left:266px;top:1628px;width:444px;height:314px;background:linear-gradient(180deg,#e6e6e6 0%,#bdbdbd 50%,#f1f1f1 100%)" role="img" aria-label="Studio Forma brand banner hanging under a slatted ceiling"></div>
  <div class="tile" style="left:719px;top:1628px;width:215px;height:152px;background:#d6d6d6" role="img" aria-label="Crumble Co packaging mark on a grey backdrop"></div>
  <div class="tile" style="left:719px;top:1789px;width:215px;height:153px;background:linear-gradient(135deg,#7fa593 0%,#e9e1dc 50%,#b77a84 100%)" role="img" aria-label="Tablet and phone showing a shop website"></div>
  <div class="tile" style="left:266px;top:1951px;width:215px;height:152px;background:linear-gradient(135deg,#cfd4d9 0%,#eef0f2 55%,#3d4249 100%)" role="img" aria-label="Laptop and phone showing a dashboard app"></div>
  <div class="tile tile-name" style="left:266px;top:2115px;width:215px;height:152px;background:#0d0d0d">VELOCITE</div>
  <div class="tile" style="left:492px;top:1951px;width:442px;height:316px;background:linear-gradient(180deg,#efe7de 0%,#e5dccf 100%)" role="img" aria-label="Hirely landing page mockup for hiring professionals"></div>

  <a class="abs btn btn-red" style="left:463px;top:2288px;width:130px;height:32px;font-size:11px">Get in touch</a>
  <a class="abs btn btn-outline" style="left:604px;top:2288px;width:133px;height:32px;font-size:11px">See more</a>
</section>

<!-- HOW WE WORK -->
<section>
  <div class="work"></div>
  <h2 class="work-title">How We Work</h2>
  <p class="work-intro">All engagements are different and we treat them that way. We work with our clients to customize a scope of work that will provide them with optimal business impact, whether that means full project ownership or close collaboration with an existing team.</p>

  <div class="step" style="left:163px">
    <svg width="104" height="104" viewBox="0 0 104 104" aria-hidden="true">
      <g fill="var(--red)" transform="translate(52 52)">
        <rect x="-11" y="-52" width="22" height="104"/>
        <rect x="-11" y="-52" width="22" height="104" transform="rotate(45)"/>
        <rect x="-11" y="-52" width="22" height="104" transform="rotate(90)"/>
        <rect x="-11" y="-52" width="22" height="104" transform="rotate(135)"/>
      </g>
    </svg>
    <h4>Strategize</h4>
    <p>Lorem ipsum dolor sit amet, consectetur adipiscing elit, sed do eiusmod tempor incididunt ut labore et dolore magna aliqua. Ut enim ad minim veniam, quis nostrud exercitation ullamco laboris nisi ut aliquip ex ea commodo consequat.</p>
  </div>
  <div class="step" style="left:458px">
    <svg width="104" height="104" viewBox="0 0 104 104" aria-hidden="true">
      <path d="M8 0 L96 52 L8 104 Z M30 36 L30 68 L58 52 Z" fill="var(--red)" fill-rule="evenodd"/>
    </svg>
    <h4>Execute</h4>
    <p>Lorem ipsum dolor sit amet, consectetur adipiscing elit, sed do eiusmod tempor incididunt ut labore et dolore magna aliqua. Ut enim ad minim veniam, quis nostrud exercitation ullamco laboris nisi ut aliquip ex ea commodo consequat.</p>
  </div>
  <div class="step" style="left:756px">
    <svg width="104" height="104" viewBox="0 0 104 104" aria-hidden="true">
      <circle cx="52" cy="52" r="40" fill="none" stroke="var(--red)" stroke-width="22"/>
    </svg>
    <h4>Optimize</h4>
    <p>Lorem ipsum dolor sit amet, consectetur adipiscing elit, sed do eiusmod tempor incididunt ut labore et dolore magna aliqua. Ut enim ad minim veniam, quis nostrud exercitation ullamco laboris nisi ut aliquip ex ea commodo consequat.</p>
  </div>
</section>

<!-- TESTIMONIAL -->
<section>
  <div class="person" role="img" aria-label="Portrait of a partner in a navy suit and striped tie"></div>
  <svg class="abs" style="left:455px;top:3018px" width="140" height="108" viewBox="0 0 140 108" aria-hidden="true">
    <g fill="#d6d6d6">
      <circle cx="32" cy="74" r="30"/><path d="M4 72 C4 30 28 6 62 2 L62 18 C40 24 28 40 30 60 Z"/>
      <circle cx="102" cy="74" r="30"/><path d="M74 72 C74 30 98 6 132 2 L132 18 C110 24 98 40 100 60 Z"/>
    </g>
  </svg>
  <h2 class="t-title">Real Testimonials<br>from our partners</h2>
  <p class="t-quote">It was good to work with you. There are very few true professional organizations such as yours, in this industry. I wish you all the best and I would indeed enjoy working with you again.</p>
  <p class="t-name">Daniel Hartley<br><span style="font-weight:400">Head of Infrastructure Services - Corvix Systems</span></p>
  <span class="arrow" style="left:976px"><svg width="26" height="26" viewBox="0 0 26 26" aria-hidden="true"><path d="M15 8 L10 13 L15 18" fill="none" stroke="#fff" stroke-width="2"/></svg></span>
  <span class="arrow" style="left:1009px"><svg width="26" height="26" viewBox="0 0 26 26" aria-hidden="true"><path d="M11 8 L16 13 L11 18" fill="none" stroke="#fff" stroke-width="2"/></svg></span>
</section>

<!-- CONTACT -->
<section>
  <div class="band-red"></div>
  <div class="contact"></div>
  <p class="c-kicker">CONTACT US TODAY</p>
  <h2 class="c-title">We want to help you<br>transform your business.</h2>
  <p class="c-text">Call us at +61 2 5550 1847 today. Fill out our contact form, or visit us.</p>
  <p class="c-addr">Level 12, Harbour Point,<br>88 Wattle Lane,<br>Sydney NSW 2000 Australia</p>
  <div class="social" style="left:479px;top:3713px"><span></span><span></span><span></span><span></span></div>

  <span class="field-label" style="left:610px;top:3471px">Your Name</span>
  <span class="field" style="left:610px;top:3488px;width:189px;height:32px"></span>
  <span class="field-label" style="left:807px;top:3471px">Company</span>
  <span class="field" style="left:807px;top:3488px;width:191px;height:32px"></span>
  <span class="field-label" style="left:610px;top:3531px">Email Address</span>
  <span class="field" style="left:610px;top:3547px;width:189px;height:32px"></span>
  <span class="field-label" style="left:807px;top:3531px">Phone</span>
  <span class="field" style="left:807px;top:3547px;width:191px;height:32px"></span>
  <span class="field-label" style="left:610px;top:3591px">Email Address</span>
  <span class="field" style="left:610px;top:3608px;width:388px;height:81px"></span>
  <a class="abs btn btn-red" style="left:610px;top:3705px;width:109px;height:29px;font-size:9px">Get in touch</a>
</section>

<!-- FOOTER -->
<footer>
  <div class="footer"></div>
  <p class="f-about">We help you make sure that an incident won’t affect in your business by providing you with the industry skills, expertise and knowledge to ensure that your business goes beyond mere compliance to business continuity and recovery standards, through to a workable plan.</p>
  <ul class="f-links" style="left:509px;top:3875px">
    <li>HOME</li><li>ABOUT</li><li>SERVICES</li><li>CLIENTS</li><li>RESOURCES</li><li>BLOG</li><li>CONTACT</li>
  </ul>
  <ul class="f-links" style="left:610px;top:3875px">
    <li>TESTIMONIALS</li><li>MEET THE TEAM</li><li>PARTNERS</li><li>FAQ</li>
  </ul>
  <div class="social" style="left:952px;top:3886px"><span></span><span></span><span></span><span></span></div>
  <p class="f-contact">+61 2 5550 1847<br><br>Level 12, Harbour Point,<br>88 Wattle Lane,<br>Sydney NSW 2000 Australia</p>
  <div class="brand" style="left:838px;top:4052px">
    <span class="brand-dot"></span>
    <div>
      <div class="brand-name">taskharbor</div>
      <div class="brand-tag">your trusted advisor</div>
    </div>
  </div>
  <p class="f-copy">© Copyright 2021. TASKHARBOR. All Rights Reseved.</p>
</footer>

</body>
</html>
```